Business Card Design for Coaching business

Looking for a simple Business card design that aligns with my website @ keenpathway.ca - very simple but specific.

Target Market(s)

Leaders looking for Organizational one on one, team and group coaching

Industry/Entity Type

Organizational Coaching

Contact Information for Business Card

one side portrait, with logo, business name and tag line on it. Keen Pathway Coaching as the Compass. The other side name, title and QR code only. Marisol Fenwick-Dorne Founder & Coach. Black background and partial view of colourful flower, to match the website.

Colors

Designer to choose only greyscale colors for use in the design.

Requirements
Must have
• black background. point of interest with partal flower to match website. QR code for website

```html
<!DOCTYPE html>
<html lang="en">
<head>
<meta charset="utf-8">
<title>Keen Pathway — Business Card Options</title>
<link rel="stylesheet" href="https://fonts.googleapis.com/css2?family=Montserrat:wght@400;600&family=Questrial&display=swap">
<style>
  :root {
    --board-grey: #878787;
    --card-black: #000000;
    --ink-white: #ffffff;
    --tagline-grey: #cfcfcf;
    --label-ink: #111111;
    --leaf-green: 30, 58, 14;
    --leaf-light: 70, 100, 40;
    --petal-red: 58, 4, 10;
    --petal-orange: 90, 34, 10;
  }
  * { margin: 0; padding: 0; box-sizing: border-box; }
  html, body {
    width: 820px;
    height: 1200px;
    overflow: hidden;
    background: var(--board-grey);
  }
  .board {
    position: relative;
    width: 820px;
    height: 1200px;
  }
  .option {
    position: absolute;
    left: 158px;
    width: 504px;
  }
  .option--one { top: 107px; }
  .option--two { top: 456px; }
  .option--three { top: 805px; }
  .card-front {
    position: relative;
    width: 504px;
    height: 288px;
    border-radius: 15px;
    overflow: hidden;
    background: var(--card-black);
  }
  .flower-backdrop {
    position: absolute;
    inset: 0;
    --leaf-a: .4;
    --petal-a: .35;
    background:
      radial-gradient(ellipse 60px 110px at 105px 130px, rgba(var(--leaf-green), var(--leaf-a)), transparent 72%),
      radial-gradient(ellipse 50px 130px at 165px 60px, rgba(var(--leaf-green), calc(var(--leaf-a) * .8)), transparent 72%),
      radial-gradient(ellipse 40px 100px at 385px 150px, rgba(var(--leaf-light), var(--leaf-a)), transparent 72%),
      radial-gradient(ellipse 80px 140px at 360px 190px, rgba(var(--leaf-green), calc(var(--leaf-a) * .8)), transparent 72%),
      radial-gradient(ellipse 150px 80px at 330px 10px, rgba(var(--petal-red), var(--petal-a)), transparent 72%),
      radial-gradient(ellipse 70px 60px at 495px 20px, rgba(var(--petal-orange), var(--petal-a)), transparent 72%);
  }
  .option--two .flower-backdrop { --leaf-a: .65; --petal-a: .6; }
  .option--three .flower-backdrop { --leaf-a: .95; --petal-a: .95; }
  .brand {
    position: absolute;
    left: 0;
    right: 0;
    top: 66px;
    display: flex;
    flex-direction: column;
    align-items: center;
  }
  .brand-circle {
    width: 106px;
    height: 106px;
    border: 4px solid var(--ink-white);
    border-radius: 50%;
  }
  .brand-name {
    margin-top: 6px;
    font-family: "Montserrat", sans-serif;
    font-weight: 600;
    font-size: 26px;
    line-height: 25px;
    color: var(--ink-white);
    text-align: center;
    text-transform: uppercase;
  }
  .tagline {
    position: absolute;
    left: 0;
    right: 0;
    top: 251px;
    font-family: "Montserrat", sans-serif;
    font-weight: 400;
    font-size: 10px;
    letter-spacing: .2px;
    color: var(--tagline-grey);
    text-align: center;
    text-transform: uppercase;
  }
  .option-label {
    margin-top: 17px;
    font-family: "Questrial", sans-serif;
    font-size: 24px;
    color: var(--label-ink);
    text-align: center;
    letter-spacing: .5px;
  }
</style>
</head>
<body>
<main class="board">
  <section class="option option--one">
    <div class="card-front">
      <div class="flower-backdrop" role="img" aria-label="Faint close-up of green leaves and a red flower petal on black"></div>
      <div class="brand">
        <div class="brand-circle"></div>
        <p class="brand-name">Keen<br>Pathway</p>
      </div>
      <p class="tagline">Coaching as the Compass</p>
    </div>
    <p class="option-label">Option 01</p>
  </section>
  <section class="option option--two">
    <div class="card-front">
      <div class="flower-backdrop" role="img" aria-label="Close-up of green leaves and a red flower petal on black"></div>
      <div class="brand">
        <div class="brand-circle"></div>
        <p class="brand-name">Keen<br>Pathway</p>
      </div>
      <p class="tagline">Coaching as the Compass</p>
    </div>
    <p class="option-label">Option 02</p>
  </section>
  <section class="option option--three">
    <div class="card-front">
      <div class="flower-backdrop" role="img" aria-label="Vivid close-up of green leaves and a red-orange flower petal on black"></div>
      <div class="brand">
        <div class="brand-circle"></div>
        <p class="brand-name">Keen<br>Pathway</p>
      </div>
      <p class="tagline">Coaching as the Compass</p>
    </div>
    <p class="option-label">Option 03</p>
  </section>
</main>
</body>
</html>
```